New Business card design to reflect rebrand

I would like a business card design with a good base colour for our new logo and also a placeholder for a profile pic of the card holder. the design needs to be editable to the point that we can easily change the picture of the person and use that design for printmoor etc. we are looking at a metalic finish business card so will need a good base colour to bring out the finish.

Target Market(s)

prospective customers

Industry/Entity Type

Business

Contact Information for Business Card

I would like one editable design that we can change the name of the card holder and profile picture. The design need to be in a format that be send to printmoor etc.

Our address is Fenwick Lodge, Mill Lane, Ashcombe Green, RG41 3TQ Tel no. 01632 960417

Requirements
Must have
• place holder for a profile pic for the card holder. in AI or preferably PSD format

```html
<!DOCTYPE html>
<html lang="en">
<head>
<meta charset="utf-8">
<title>Corvane Business Card</title>
<link rel="stylesheet" href="https://fonts.googleapis.com/css2?family=Montserrat:wght@400;500;700&display=swap">
<style>
  :root {
    --backdrop: #5b5b5b;
    --card: #f6f6f4;
    --card-shade: #e9e9e6;
    --blue: #4c6a8c;
    --orange: #e8822e;
    --photo-top: #c9ccd0;
    --photo-bottom: #8d949c;
  }
  * { margin: 0; padding: 0; box-sizing: border-box; }
  html, body { width: 1200px; height: 902px; overflow: hidden; }
  body {
    background: var(--backdrop);
    font-family: "Montserrat", sans-serif;
    position: relative;
  }
  .card {
    position: absolute;
    top: 276px;
    width: 520px;
    height: 316px;
    background: linear-gradient(135deg, var(--card) 0%, var(--card-shade) 100%);
    box-shadow: 0 14px 30px rgba(0,0,0,.35);
  }
  .card--front { left: 50px; }
  .card--back { left: 630px; }

  /* front */
  .brand {
    position: absolute;
    color: var(--blue);
    font-weight: 700;
    letter-spacing: 3px;
    display: flex;
    align-items: center;
    gap: 10px;
  }
  .brand__dot {
    width: 14px; height: 14px;
    border-radius: 50%;
    background: var(--orange);
  }
  .card--front .brand { left: 36px; top: 48px; font-size: 30px; }
  .portrait {
    position: absolute;
    right: 30px; top: 26px;
    width: 150px; height: 124px;
    border: 3px solid var(--orange);
    background: linear-gradient(180deg, var(--photo-top), var(--photo-bottom));
  }
  .front-bar {
    position: absolute;
    right: 30px; bottom: 0;
    width: 150px; height: 6px;
    background: var(--orange);
  }
  .holder { position: absolute; left: 36px; top: 150px; }
  .holder__name { color: var(--blue); font-size: 19px; font-weight: 500; }
  .holder__role { color: var(--orange); font-size: 13px; font-weight: 500; margin-top: 3px; }
  .contact {
    position: absolute; left: 36px; top: 214px;
    color: var(--orange);
    font-size: 11.5px;
    line-height: 17px;
  }
  .contact__address { margin-bottom: 8px; }
  .contact__row span:first-child { display: inline-block; width: 22px; }

  /* back */
  .card--back .brand {
    left: 0; right: 0; top: 118px;
    justify-content: center;
    font-size: 40px;
  }
  .web {
    position: absolute; left: 0; right: 0; top: 210px;
    display: flex; align-items: center; justify-content: center; gap: 14px;
    color: var(--blue);
    font-size: 13px;
    letter-spacing: 1px;
  }
  .web__rule { width: 46px; height: 2px; background: var(--orange); }
</style>
</head>
<body>
  <section class="card card--front">
    <div class="brand"><span class="brand__dot"></span>CORVANE</div>
    <div class="portrait" role="img" aria-label="Profile photo placeholder for the card holder"></div>
    <div class="front-bar"></div>
    <div class="holder">
      <div class="holder__name">Names surname</div>
      <div class="holder__role">Your Position</div>
    </div>
    <div class="contact">
      <div class="contact__address">Fenwick Lodge, Mill Lane,<br>Ashcombe Green, RG41 3TQ</div>
      <div class="contact__row"><span>T</span><span>: 01632 960417</span></div>
      <div class="contact__row"><span>M</span><span>: 07700 900218</span></div>
      <div class="contact__row"><span>E</span><span>: name@corvane-ws.com</span></div>
    </div>
  </section>

  <section class="card card--back">
    <div class="brand"><span class="brand__dot"></span>CORVANE</div>
    <div class="web"><span class="web__rule"></span><span>www.corvane-ws.com</span><span class="web__rule"></span></div>
  </section>
</body>
</html>
```